Business Card Design Project

We consult with hotels on setting rates and maximizing a revenue strategy

Industry/Entity Type

Business

Contact Information for Business Card

I am not sure what I want. Our company offers high level consulting to hotels around the country but we are also laid back. I would like something that is professional but also shows the laid back side

```html
<!DOCTYPE html>
<html lang="en">
<head>
<meta charset="utf-8">
<title>Harborline Revenue Management Solutions – Business Card</title>
<link href="https://fonts.googleapis.com/css2?family=Open+Sans:wght@400;600;700&display=swap" rel="stylesheet">
<style>
  :root {
    --page-bg: #e4e5e7;
    --card-blue: #5a7389;
    --card-blue-light: #6a8399;
    --card-blue-dark: #4e6679;
    --gold: #d2c49c;
    --gold-ring: #a8976a;
    --ink-dark: #2f3438;
    --text-light: #e9ecef;
    --text-muted: #c9c1a6;
    --icon: #2c3640;
  }
  * { box-sizing: border-box; margin: 0; padding: 0; }
  html, body {
    width: 1200px; height: 1000px; overflow: hidden;
    background: var(--page-bg);
    font-family: "Open Sans", sans-serif;
  }
  .canvas {
    position: relative; width: 1200px; height: 1000px;
    display: flex; justify-content: center; align-items: center; gap: 110px;
  }
  .card {
    position: relative; width: 380px; height: 665px;
    background: linear-gradient(160deg, var(--card-blue-light), var(--card-blue) 45%, var(--card-blue-dark));
    box-shadow: 0 10px 30px rgba(0,0,0,0.18);
    overflow: hidden;
  }

  /* Front */
  .brand {
    position: absolute; left: 46px; top: 78px;
    display: flex; align-items: center; gap: 14px;
  }
  .brand-dot {
    width: 46px; height: 46px; border-radius: 50%;
    background: var(--gold);
  }
  .brand-text { display: flex; flex-direction: column; }
  .brand-name {
    font-weight: 700; font-size: 30px; letter-spacing: 1px;
    color: var(--ink-dark); line-height: 1;
  }
  .brand-tagline {
    font-weight: 600; font-size: 12px; color: var(--ink-dark);
    margin-top: 6px;
  }
  .brand-web {
    font-weight: 600; font-size: 12px; color: var(--ink-dark);
    margin-top: 2px;
  }
  .name-band {
    position: absolute; left: 0; top: 250px; width: 100%; height: 48px;
    background: var(--gold);
    display: flex; align-items: center; padding-left: 40px;
  }
  .person-name {
    font-size: 26px; font-weight: 400; color: #ffffff;
  }
  .person-title {
    position: absolute; left: 42px; top: 308px;
    font-size: 13px; color: var(--text-muted);
  }
  .contact-list {
    position: absolute; left: 46px; top: 420px;
    list-style: none;
  }
  .contact-item {
    display: flex; align-items: center; gap: 14px;
    height: 42px; font-size: 14px; letter-spacing: 1px;
    color: var(--text-light);
  }
  .contact-icon { width: 18px; height: 18px; flex: none; }

  /* Back */
  .seal {
    position: absolute; left: 50%; top: 50%;
    width: 270px; height: 270px; margin: -135px 0 0 -135px;
    border-radius: 50%;
    background: var(--gold);
    border: 5px solid var(--gold-ring);
    display: flex; flex-direction: column; justify-content: center; align-items: center;
    text-align: center;
  }
  .seal .brand-name { font-size: 28px; }
  .seal .brand-tagline { font-size: 11px; }
  .seal .brand-web { font-size: 11px; }
</style>
</head>
<body>
<main class="canvas">
  <section class="card card-front" aria-label="Card front">
    <div class="brand">
      <span class="brand-dot"></span>
      <div class="brand-text">
        <span class="brand-name">HARBORLINE</span>
        <span class="brand-tagline">Revenue Management Solutions</span>
        <span class="brand-web">www.HarborlineRMS.com</span>
      </div>
    </div>

    <div class="name-band"><span class="person-name">Dana Whitmore</span></div>
    <p class="person-title">Regional Revenue Manager</p>

    <ul class="contact-list">
      <li class="contact-item">
        <svg class="contact-icon" viewBox="0 0 18 18" aria-hidden="true"><rect x="5" y="1" width="8" height="16" rx="2" fill="var(--icon)"/><rect x="6.5" y="3" width="5" height="7" fill="var(--card-blue)"/></svg>
        503-555-0142
      </li>
      <li class="contact-item">
        <svg class="contact-icon" viewBox="0 0 18 18" aria-hidden="true"><rect x="4" y="1" width="10" height="5" fill="var(--icon)"/><rect x="1" y="6" width="16" height="7" rx="1.5" fill="var(--icon)"/><rect x="4" y="11" width="10" height="6" fill="var(--icon)"/><rect x="5.5" y="12.5" width="7" height="3" fill="var(--card-blue)"/></svg>
        503-555-0187
      </li>
      <li class="contact-item">
        <svg class="contact-icon" viewBox="0 0 18 18" aria-hidden="true"><rect x="1" y="3.5" width="16" height="11" fill="none" stroke="var(--icon)" stroke-width="1.6"/><path d="M1 3.5 L9 10 L17 3.5" fill="none" stroke="var(--icon)" stroke-width="1.6"/></svg>
        Dana@HarborlineRMS.com
      </li>
      <li class="contact-item">
        <svg class="contact-icon" viewBox="0 0 18 18" aria-hidden="true"><circle cx="9" cy="9" r="7.5" fill="var(--icon)"/><ellipse cx="9" cy="9" rx="3" ry="7.5" fill="none" stroke="var(--card-blue)" stroke-width="1"/><line x1="1.5" y1="9" x2="16.5" y2="9" stroke="var(--card-blue)" stroke-width="1"/></svg>
        www.HarborlineRMS.com
      </li>
    </ul>
  </section>

  <section class="card card-back" aria-label="Card back">
    <div class="seal">
      <span class="brand-name">HARBORLINE</span>
      <span class="brand-tagline">Revenue Management Solutions</span>
      <span class="brand-web">www.HarborlineRMS.com</span>
    </div>
  </section>
</main>
</body>
</html>
```